AUSTRALIAN CONSULTING FIRM BUSINESS CARD - MODERN

We are wanting a modern, clean lined business card design. We are professional niche consultancy firm situated in Australia called Harbrook Advisory Partners Pty Ltd.
The card should communicate professionalism and creativity and draw on our logo design (attached).
The design should be two sided, landscape orientation.
Target Market(s)
government, not for profit sector, corporate clients
Industry/Entity Type
Landscape
Requirements
Must have
- logo
no new introduced colours

```html
<!DOCTYPE html>
<html lang="en">
<head>
<meta charset="utf-8">
<title>Harbrook Advisory Partners – Business Card</title>
<link href="https://fonts.googleapis.com/css2?family=Roboto+Condensed:wght@700&family=Arimo:wght@400&display=swap" rel="stylesheet">
<style>
  :root {
    --stage: #393431;
    --card-front: #ffffff;
    --card-back: #dedede;
    --navy: #27307a;
    --blue: #1e8fd5;
    --rule: #c98aa6;
    --ink: #1c1c1c;
    --ink-soft: #333333;
  }
  html, body {
    margin: 0;
    padding: 0;
    width: 1159px;
    height: 1200px;
    overflow: hidden;
    background: var(--stage);
  }
  .stage {
    position: relative;
    width: 1159px;
    height: 1200px;
  }
  .card {
    position: absolute;
    left: 231px;
    width: 677px;
    height: 365px;
    overflow: hidden;
    box-shadow: 0 1px 2px rgba(0,0,0,0.35);
  }
  .card--front { top: 222px; background: var(--card-front); border-radius: 2px; }
  .card--back  { top: 594px; background: var(--card-back); }

  .rule {
    position: absolute;
    height: 1px;
  }
  .rule--top {
    top: 106px;
    left: 0;
    width: 340px;
    background: linear-gradient(to right, var(--rule), rgba(201,138,166,0));
  }
  .rule--bottom {
    top: 258px;
    right: 0;
    width: 340px;
    background: linear-gradient(to left, var(--rule), rgba(201,138,166,0));
  }

  .brand {
    position: absolute;
    top: 0;
    left: 0;
    width: 100%;
    height: 100%;
    display: flex;
    align-items: center;
    justify-content: center;
    gap: 14px;
  }
  .brand__dot {
    width: 30px;
    height: 30px;
    border-radius: 50%;
    background: var(--blue);
    flex: none;
  }
  .brand__name {
    font-family: "Roboto Condensed", "Arial Narrow", sans-serif;
    font-weight: 700;
    font-size: 29px;
    letter-spacing: 0.5px;
    color: var(--navy);
    margin: 0;
    white-space: nowrap;
  }

  .details {
    position: absolute;
    top: 150px;
    left: 0;
    width: 100%;
    text-align: center;
  }
  .details__company {
    font-family: "Roboto Condensed", "Arial Narrow", sans-serif;
    font-weight: 700;
    font-size: 24px;
    color: var(--ink);
    margin: 0 0 14px;
    letter-spacing: 0.2px;
  }
  .details__line {
    font-family: "Arimo", Arial, sans-serif;
    font-size: 18px;
    line-height: 26px;
    color: var(--ink-soft);
    margin: 0;
  }
</style>
</head>
<body>
  <main class="stage">
    <section class="card card--front" aria-label="Card front">
      <div class="rule rule--top"></div>
      <div class="rule rule--bottom"></div>
      <div class="brand">
        <span class="brand__dot"></span>
        <h1 class="brand__name">HARBROOK ADVISORY PARTNERS PTY LTD</h1>
      </div>
    </section>

    <section class="card card--back" aria-label="Card back">
      <div class="details">
        <h2 class="details__company">HARBROOK ADVISORY PARTNERS PTY LTD.</h2>
        <p class="details__line">Tel :02-555-0147, E-mail : info@harbrookadvisory.com,</p>
        <p class="details__line">Web : www.harbrookadvisory.com</p>
      </div>
    </section>
  </main>
</body>
</html>
```